Dalton Power Supply, Inc. Business Card Design

We are an Electrical Distributor looking for a Modern, Professional Business Card design.

Target Market(s)

Residential Commercial Industrial

Industry/Entity Type

Electrical

Contact Information for Business Card

Dalton Power Supply, Inc.
418 Maple Ridge Lane
Brookvale, NC 27514
555-214-7630
555-214-8842 Fax
daltonpower@brightmail-example.net

```html
<!DOCTYPE html>
<html lang="en">
<head>
<meta charset="utf-8">
<title>Dalton Power Supply, Inc. – Business Card</title>
<link rel="stylesheet" href="https://fonts.googleapis.com/css2?family=Nunito+Sans:wght@400;900&display=swap">
<style>
  :root {
    --sky: #4ae0f2;
    --floor: #abc2c3;
    --paper: #eceff2;
    --ink: #111111;
    --text: #1c1c1c;
    --rule-dark: #3a3d42;
    --rule-accent: #58e6ee;
  }
  * { margin: 0; padding: 0; box-sizing: border-box; }
  html, body {
    width: 1200px;
    height: 685px;
    overflow: hidden;
    background: var(--paper);
  }
  .card {
    position: relative;
    width: 1200px;
    height: 685px;
    background: var(--paper);
    font-family: "Nunito Sans", Arial, sans-serif;
  }
  .hero-art {
    position: absolute;
    left: 0;
    top: 0;
    width: 471px;
    height: 685px;
    background: linear-gradient(to bottom, var(--sky) 0, var(--sky) 547px, var(--floor) 547px, var(--floor) 100%);
  }
  .brand {
    position: absolute;
    left: 600px;
    top: 150px;
    width: 545px;
    color: var(--ink);
    font-weight: 900;
    text-transform: uppercase;
    text-align: right;
  }
  .brand-name {
    display: block;
    font-size: 108px;
    line-height: 1;
    letter-spacing: 2px;
  }
  .brand-sub {
    display: block;
    margin-top: 22px;
    font-size: 44px;
    line-height: 1;
    letter-spacing: 0.5px;
  }
  .divider {
    position: absolute;
    left: 616px;
    top: 358px;
    width: 517px;
    height: 4px;
    display: flex;
  }
  .divider-accent { width: 173px; background: var(--rule-accent); }
  .divider-main { flex: 1; background: var(--rule-dark); }
  .contact {
    position: absolute;
    right: 63px;
    top: 383px;
    list-style: none;
    text-align: right;
    color: var(--text);
    font-size: 31px;
    font-weight: 400;
    line-height: 45px;
  }
</style>
</head>
<body>
  <div class="card">
    <div class="hero-art" role="img" aria-label="Illustration of a large white light bulb standing on a grey floor against a bright cyan wall"></div>

    <h1 class="brand">
      <span class="brand-name">Dalton</span>
      <span class="brand-sub">Power Supply, Inc.</span>
    </h1>

    <div class="divider" aria-hidden="true">
      <span class="divider-accent"></span>
      <span class="divider-main"></span>
    </div>

    <ul class="contact">
      <li>418 Maple Ridge Lane</li>
      <li>Brookvale, NC 27514</li>
      <li>Phone: 555-214-7630</li>
      <li>Fax: 555-214-8842</li>
      <li>daltonpower@brightmail-example.net</li>
    </ul>
  </div>
</body>
</html>
```